Business Card Design Project

Hi I am after a business card double sided 1 side to have the attached PDF on front on the back:

Tavi Rundell - Managing Director
Mobile: 0412 638 274
email: tavi@pruvo.com.au
web: www.pruvo.com.au

Industry/Entity Type

Business

Font styles to use
Sans Serif

Requirements
Must have
• I want a classy looking card
Nice to have
• I like lime green and black and white

```html
<!DOCTYPE html>
<html lang="en">
<head>
<meta charset="UTF-8">
<title>Pruvo Lawns and Gardens – Business Card</title>
<link href="https://fonts.googleapis.com/css2?family=Questrial&display=swap" rel="stylesheet">
<style>
  :root {
    --lime: #2fb52a;
    --lime-bright: #3ccf32;
    --card-black: #221e1f;
    --card-white: #ffffff;
    --paper-shade: #f1f1f1;
    --ink: #231f20;
    --ink-soft: #4a4a4a;
    --backdrop: #e6e6e3;
  }
  * { box-sizing: border-box; margin: 0; padding: 0; }
  html, body { width: 1200px; height: 951px; overflow: hidden; }
  body {
    background: var(--backdrop);
    font-family: "Questrial", "Century Gothic", sans-serif;
    position: relative;
  }
  .card {
    position: absolute;
    width: 560px;
    height: 341px;
    border-radius: 22px;
    overflow: hidden;
    box-shadow: 0 10px 26px rgba(0,0,0,0.22);
  }

  /* Front side */
  .card--front {
    left: 110px; top: 80px;
    background: var(--card-black);
    border-left: 10px solid var(--lime);
    border-right: 22px solid var(--lime);
  }
  .card--front .brand {
    position: absolute;
    left: 0; right: 0; top: 122px;
    display: flex; align-items: center; justify-content: center; gap: 16px;
  }
  .brand__square {
    width: 44px; height: 44px; border-radius: 6px;
    background: var(--lime-bright);
    flex: none;
  }
  .brand__name {
    font-size: 30px;
    letter-spacing: 0.2px;
    color: #ffffff;
    white-space: nowrap;
  }
  .card--front .web {
    position: absolute; left: 0; right: 0; bottom: 52px;
    text-align: center;
    color: #e8e8e8;
    font-size: 17px;
    letter-spacing: 1.5px;
  }

  /* Back side */
  .card--back {
    left: 520px; top: 530px;
    background: linear-gradient(180deg, var(--card-white) 0%, var(--paper-shade) 78%);
  }
  .card--back .brand {
    position: absolute; left: 32px; top: 126px;
    width: 272px;
    display: flex; align-items: center; gap: 10px;
  }
  .card--back .brand__square { width: 32px; height: 32px; border-radius: 5px; }
  .card--back .brand__name { color: var(--ink); font-size: 18px; }
  .divider {
    position: absolute; left: 326px; top: 30px;
    width: 2px; height: 232px;
    background: linear-gradient(180deg, rgba(47,181,42,0) 0%, var(--lime) 50%, rgba(47,181,42,0) 100%);
    opacity: 0.55;
  }
  .person { position: absolute; left: 350px; top: 78px; }
  .person__name { font-size: 21px; color: var(--ink); letter-spacing: 0.4px; }
  .person__title { font-size: 14px; color: var(--ink-soft); margin-top: 4px; }
  .contacts {
    position: absolute; left: 350px; top: 172px;
    list-style: none;
  }
  .contacts li {
    display: flex; align-items: center; gap: 10px;
    font-size: 15px; color: var(--ink);
    height: 24px;
    white-space: nowrap;
  }
  .contacts svg { width: 16px; height: 16px; flex: none; }
  .foot-rule {
    position: absolute; left: 0; right: 0; bottom: 46px;
    height: 2px; background: var(--ink);
  }
  .foot-band {
    position: absolute; left: 0; right: 0; bottom: 0;
    height: 40px; background: var(--lime-bright);
  }
</style>
</head>
<body>

  <section class="card card--front" aria-label="Card front">
    <div class="brand">
      <span class="brand__square"></span>
      <span class="brand__name">Pruvo Lawns and Gardens</span>
    </div>
    <p class="web">www.pruvo.com.au</p>
  </section>

  <section class="card card--back" aria-label="Card back">
    <div class="brand">
      <span class="brand__square"></span>
      <span class="brand__name">Pruvo Lawns and Gardens</span>
    </div>
    <div class="divider"></div>
    <div class="person">
      <p class="person__name">Tavi Rundell</p>
      <p class="person__title">Managing Director</p>
    </div>
    <ul class="contacts">
      <li>
        <svg viewBox="0 0 16 16" aria-hidden="true"><rect x="4" y="1" width="8" height="14" rx="2" fill="var(--lime)"/><rect x="5.5" y="3" width="5" height="7" fill="#fff"/><circle cx="8" cy="12.5" r="1" fill="#fff"/></svg>
        <span>0412 638 274</span>
      </li>
      <li>
        <svg viewBox="0 0 16 16" aria-hidden="true"><rect x="1" y="3" width="14" height="10" rx="2" fill="var(--lime)"/><path d="M2 4.5 L8 9 L14 4.5" stroke="#fff" stroke-width="1.4" fill="none"/></svg>
        <span>tavi@pruvo.com.au</span>
      </li>
      <li>
        <svg viewBox="0 0 16 16" aria-hidden="true"><circle cx="8" cy="8" r="7" fill="var(--lime)"/></svg>
        <span>www.pruvo.com.au</span>
      </li>
    </ul>
    <div class="foot-rule"></div>
    <div class="foot-band"></div>
  </section>

</body>
</html>
```